Startup Technology Consulting Firm in NYC Needs A Website

I need a website built for my startup technology consulting company Larkspur Systems Group. We offer a unique white glove service that provides end to end technology support. I want to stand out above the rest. We are small firm but are very dedicated which where we derive our name from LSG primarily offers
end to end technology advisory services to small businesses lacking their own IT staff. We offer top notch white glove and our customer service and satisfaction is exceed by no one.

Below are some of what we provide our clients

Strategic IT Planning
Business Continuity Planning/Disaster Recovery
Cloud Computing\DataCenter Solutions
Server Infrastructure/Networking
Virtualization Technologies
Project Management

Our Technology Advisors hold many certifications from Quorvane & Zelpix. We are also Quorvane Partners

I have attached my logo (preview design) As soon as I ge the final images I will upload.

Industry/Entity Type

Information Technology

Coding

Coded - Design and coding required

Number of Pages Required

1 page

Font styles to use
Sans Serif

Requirements
Must have
• Attract Target Market. The site should bleed the company vision
• DEDICATION everything about the site should show this
• Layout the Benefits of our offerings
• Links to my social media
• Links to dircct my client's for remote support

```html
<!DOCTYPE html>
<html lang="en">
<head>
<meta charset="utf-8">
<title>Larkspur Systems Group</title>
<link href="https://fonts.googleapis.com/css2?family=Montserrat:wght@400;500;600&family=Mulish:wght@400;600&display=swap" rel="stylesheet">
<style>
:root{
  --navy:#133a7c;
  --sky:#2aa8e0;
  --ink:#333;
  --muted:#666;
  --bar:rgba(40,40,40,.82);
  --card:#a8a8a8;
  --paper:#eeeeee;
  --line:#cfcfcf;
  --footer:#0b0b0b;
}
*{box-sizing:border-box;margin:0;padding:0}
html,body{width:675px;height:1200px;overflow:hidden;background:#fff}
body{position:relative;font-family:'Montserrat',sans-serif;color:var(--ink)}
.abs{position:absolute}
.hero{left:0;top:0;width:675px;height:395px;
  background:radial-gradient(ellipse 160px 120px at 337px 215px,rgba(255,255,255,.95),rgba(255,255,255,0) 100%),
  linear-gradient(100deg,#c9d2da 0%,#8fa4b6 22%,#d7dfe6 45%,#e7c9c9 65%,#b9b6b2 85%,#d5dbe0 100%)}
.topbar{left:0;top:8px;width:675px;height:36px;background:var(--bar);color:#fff;font-size:8.5px}
.topbar .phone{left:42px;top:12px;display:flex;align-items:center;gap:8px}
.topbar .mail{right:42px;top:12px;display:flex;align-items:center;gap:8px}
.search{left:246px;top:6px;width:176px;height:24px;background:#fff;color:#333;font-size:8px;padding:7px 7px;display:flex;justify-content:space-between}
.arrow{width:29px;height:29px;border-radius:50%;background:var(--navy);color:#fff;font-size:15px;text-align:center;line-height:27px}
.brand{left:187px;top:140px;width:300px;text-align:center;color:var(--navy);font-family:'Montserrat',sans-serif;font-weight:400}
.brand .dot{width:46px;height:46px;border-radius:50%;background:var(--sky);opacity:.7;margin:0 auto 10px}
.brand .name{font-size:18px;letter-spacing:1px;line-height:1.25}
.nav a{position:absolute;top:384px;font-size:9.5px;font-weight:500;color:var(--navy);text-decoration:none;letter-spacing:.3px}
.nav .active-line{left:88px;top:370px;width:53px;height:2px;background:var(--navy)}
.about-title{left:40px;top:426px;width:260px;text-align:center;font-family:'Mulish',sans-serif;font-size:22px;line-height:30px;color:var(--navy)}
.light{color:var(--sky)}
.vline{width:1px;background:var(--navy)}
.about-text{left:328px;top:429px;width:300px;font-size:9.2px;line-height:17px;color:#444}
.about-text a{display:inline-block;margin-top:6px;color:var(--navy);font-size:10px}
.services{left:0;top:519px;width:675px;height:193px;background:var(--paper);border-top:1px solid var(--line);border-bottom:1px solid var(--line)}
.section-title{width:675px;text-align:center;font-family:'Mulish',sans-serif;font-size:22px;color:var(--navy)}
.card{top:66px;width:190px;height:93px;background:var(--card);border-radius:3px;padding:16px 8px 0 56px;color:#222}
.card h3{font-family:'Mulish',sans-serif;font-weight:400;font-size:11px;color:var(--navy);margin-bottom:5px}
.card p{font-size:8px;line-height:13px}
.card svg{position:absolute;left:12px;top:18px}
.badge{fill:#d8d8d8}
.partner-title{left:430px;top:738px;width:160px;text-align:center;font-family:'Mulish',sans-serif;font-size:21px;color:var(--navy)}
.partner-text{left:430px;top:775px;width:160px;text-align:center;font-size:8.3px;line-height:13px;color:var(--sky)}
.contact{left:0;top:850px;width:675px;height:320px;background:var(--paper)}
.field{background:var(--paper);border:1px solid #c8c8c8;font-size:7.5px;color:#777;padding:7px 8px}
.submit{left:285px;top:1050px;width:105px;height:29px;background:var(--sky);color:#fff;font-size:10.5px;text-align:center;line-height:29px}
.follow{left:0;top:1097px;width:675px;text-align:center;font-size:10px;color:#555}
.social{top:1126px;height:24px;font-size:9.5px;text-align:center;line-height:24px;color:#444;border-bottom:1px solid #8cc7dc}
.social.primary{background:#1f5fc9;color:#fff;border:none}
.footer{left:0;top:1170px;width:675px;height:30px;background:var(--footer);color:#fff;font-size:8px;text-align:center;line-height:30px}
.footer span{color:var(--sky)}
</style>
</head>
<body>
<div class="abs hero" role="img" aria-label="Photo of a team of consultants working together around an office desk with a laptop"></div>

<div class="abs topbar">
  <div class="abs phone">
    <svg width="11" height="11" viewBox="0 0 24 24"><path fill="#2aa8e0" d="M6.6 10.8a15 15 0 0 0 6.6 6.6l2.2-2.2c.3-.3.7-.4 1-.2 1.1.4 2.3.6 3.6.6.6 0 1 .4 1 1V20c0 .6-.4 1-1 1A17 17 0 0 1 3 4c0-.6.4-1 1-1h3.5c.6 0 1 .4 1 1 0 1.3.2 2.5.6 3.6.1.3 0 .7-.2 1z"/></svg>
    +1 555 014 2290
  </div>
  <div class="abs search"><span>SEARCH</span>
    <svg width="11" height="11" viewBox="0 0 24 24"><circle cx="10" cy="10" r="7" fill="none" stroke="#222" stroke-width="3"/><path d="M15 15l6 6" stroke="#222" stroke-width="3"/></svg>
  </div>
  <div class="abs mail">
    <svg width="12" height="9" viewBox="0 0 24 18"><rect width="24" height="18" rx="2" fill="#2aa8e0"/><path d="M1 2l11 8 11-8" fill="none" stroke="#fff" stroke-width="2"/></svg>
    hello@larkspur.example
  </div>
</div>

<div class="abs arrow" style="left:8px;top:184px">&laquo;</div>
<div class="abs arrow" style="left:638px;top:184px">&raquo;</div>

<div class="abs brand">
  <div class="dot"></div>
  <div class="name">LARKSPUR<br>SYSTEMS GROUP</div>
</div>

<svg class="abs" style="left:0;top:368px" width="675" height="30" viewBox="0 0 675 30">
  <path d="M0 2 H280 C302 2 312 26 337 26 C362 26 372 2 394 2 H675 V30 H0 Z" fill="#fff"/>
</svg>

<nav class="nav">
  <div class="abs active-line"></div>
  <a style="left:98px">HOME</a>
  <a style="left:183px">ABOUT US</a>
  <a style="left:432px">SERVICES</a>
  <a style="left:527px">CONTACT US</a>
</nav>

<h1 class="abs about-title">Know About <span class="light">Larkspur Systems Group</span></h1>
<div class="abs vline" style="left:306px;top:422px;height:70px"></div>
<div class="abs about-text">
  Lorem ipsum dolor sit amet, consectetur adipiscing elit, sed do eiusmod tempor incididunt ut labore et dolore magna aliqua.<br>
  <a href="#">READ MORE</a>
</div>

<section class="abs services">
  <h2 class="abs section-title" style="top:23px">What We Do <span class="light">for Our Client</span></h2>
  <div class="abs card" style="left:43px">
    <svg width="34" height="30" viewBox="0 0 34 30"><circle cx="12" cy="14" r="8" fill="none" stroke="#fff" stroke-width="4" stroke-dasharray="3 2"/><circle cx="12" cy="14" r="3" fill="#fff"/><circle cx="27" cy="7" r="4.5" fill="none" stroke="#fff" stroke-width="2.5"/><circle cx="27" cy="23" r="4" fill="none" stroke="#fff" stroke-width="2.5"/></svg>
    <h3>Strategic IT Planning</h3>
    <p>Lorem ipsum dolor sit amet, consectetur adipiscing elit, sed do eiusmod tempor.</p>
  </div>
  <div class="abs card" style="left:242px">
    <svg width="32" height="32" viewBox="0 0 32 32"><path d="M10 14a5 5 0 0 1 9-3 4 4 0 0 1 5 4H9a3 3 0 0 1 1-1z" fill="#fff"/><path d="M2 24c4-3 8-3 12-1h6c2 0 2 3 0 3h-7M2 30c5-2 10 0 16-2l10-6" fill="none" stroke="#fff" stroke-width="2.5"/></svg>
    <h3>DataCenter Solutions</h3>
    <p>Lorem ipsum dolor sit amet, consectetur adipiscing elit, sed do eiusmod tempor.</p>
  </div>
  <div class="abs card" style="left:442px">
    <svg width="28" height="34" viewBox="0 0 28 34"><rect x="2" y="4" width="24" height="29" rx="2" fill="none" stroke="#fff" stroke-width="2.5"/><rect x="9" y="1" width="10" height="5" fill="#fff"/><path d="M7 13h14M7 18h14M7 23h14M7 28h10" stroke="#fff" stroke-width="1.6"/></svg>
    <h3>Project Management</h3>
    <p>Lorem ipsum dolor sit amet, consectetur adipiscing elit, sed do eiusmod tempor.</p>
  </div>
</section>

<svg class="abs" style="left:96px;top:746px" width="256" height="64" viewBox="0 0 256 64" role="img" aria-label="Partner certification badges">
  <rect class="badge" x="0" y="0" width="80" height="62" rx="3"/>
  <rect class="badge" x="180" y="0" width="72" height="62" rx="3"/>
</svg>
<div class="abs vline" style="left:400px;top:736px;height:88px"></div>
<h2 class="abs partner-title">Our Partner</h2>
<p class="abs partner-text">Our Technology Advisors hold many certifications from Quorvane &amp; Zelpix</p>

<section class="abs contact">
  <svg class="abs" style="left:0;top:0" width="675" height="28" viewBox="0 0 675 28">
    <path d="M0 0 H675 V1 H395 C372 1 362 26 337 26 C312 26 302 1 280 1 H0 Z" fill="#fff" stroke="#d6d6d6"/>
  </svg>
  <h2 class="abs section-title" style="top:49px">Keep In Touch <span class="light">With Us</span></h2>
  <div class="abs field" style="left:112px;top:95px;width:222px;height:22px">Name</div>
  <div class="abs field" style="left:341px;top:95px;width:222px;height:22px">Email Id</div>
  <div class="abs field" style="left:112px;top:124px;width:451px;height:70px">Message</div>
</section>
<div class="abs submit">Submit</div>
<p class="abs follow">Follow Us On</p>
<a class="abs social primary" style="left:190px;width:64px">Friendloop</a>
<a class="abs social" style="left:264px;width:62px">Chirpline</a>
<a class="abs social" style="left:341px;width:70px">Plusring</a>
<a class="abs social" style="left:423px;width:63px">Workweave</a>

<footer class="abs footer">© Larkspur Systems Group <span>- 2015. All Rights Reserved.</span></footer>
</body>
</html>
```